Owen Tasker Studios Business Card

Looking for a clear, modern, elegant, sharp business card that conveys a professional yet edgy image to my business as a wedding, portrait, and travel photographer. Would like something that looks vintage yet modern. Need a new business card to grow my business. We are growing the business for Wedding and Event Photography as well as fine art Photography. (Mostly Landscapes)
Updates

I’m looking through designs now but I have a new logo that i want using please.

New logo uploaded please redesign using that

PLEASE ALL DESIGNERS LOOK IN BRIEF FOR NEW LOGO

Target Market(s)

Brides, Grooms, Families with Kids, People looking for Fine Art Photography Artwork

Industry/Entity Type

Photographer

Contact Information for Business Card

Unsure

Font styles to use
Serif

Colors

Designer to choose colors to be used in the design.

Requirements
Must have
• My Website:
• http://taskerlens.examplefolio.net
• Phone:
• 323-481-5206
• Email:
• owentaskerlens@mailbox-example.net
Nice to have
• Would like a sort of shine on the printing finish.
• I like black I think it looks good on a business card.
• Can try working with my logo (png that I've attached)

```html
<!DOCTYPE html>
<html lang="en">
<head>
<meta charset="utf-8">
<title>Owen Tasker Studios — Business Card</title>
<link rel="stylesheet" href="https://fonts.googleapis.com/css2?family=Lato:wght@300;400;700&display=swap">
<style>
  :root {
    --stage: #1b1b1c;
    --card-deep: #050505;
    --card-sheen: #1a1b1d;
    --ink-light: #f4f4f4;
    --ink-soft: #ececec;
    --icon-glyph: #0a0a0a;
  }
  * { box-sizing: border-box; }
  html, body {
    margin: 0;
    width: 1200px;
    height: 1087px;
    overflow: hidden;
    background: var(--stage);
    font-family: "Lato", sans-serif;
  }
  .canvas {
    position: relative;
    width: 1200px;
    height: 1087px;
  }
  .card {
    position: absolute;
    left: 303px;
    width: 570px;
    height: 325px;
    background: linear-gradient(110deg, var(--card-deep) 0%, var(--card-deep) 40%, var(--card-sheen) 100%);
  }
  .card--front { top: 204px; }
  .card--back  { top: 573px; }

  .studio-title {
    position: absolute;
    left: 57px;
    top: 62px;
    margin: 0;
    font-weight: 700;
    font-size: 26.5px;
    letter-spacing: 0.08em;
    color: var(--ink-light);
    text-transform: uppercase;
    white-space: nowrap;
  }
  .contact-list {
    position: absolute;
    left: 56px;
    top: 124px;
    margin: 0;
    padding: 0;
    list-style: none;
  }
  .contact-item {
    display: flex;
    align-items: center;
    height: 32px;
    margin-bottom: 18px;
    font-weight: 300;
    font-size: 20px;
    color: var(--ink-soft);
    white-space: nowrap;
  }
  .contact-icon {
    width: 32px;
    height: 32px;
    margin-right: 16px;
    flex: none;
  }

  .logo-name {
    position: absolute;
    left: 0;
    right: 0;
    top: 0;
    bottom: 0;
    display: flex;
    align-items: center;
    justify-content: center;
    margin: 0;
    font-weight: 400;
    font-size: 30px;
    color: var(--ink-light);
    white-space: nowrap;
  }
</style>
</head>
<body>
<main class="canvas">
  <section class="card card--front" aria-label="Business card front">
    <h1 class="studio-title">Owen Tasker Studios</h1>
    <ul class="contact-list">
      <li class="contact-item">
        <svg class="contact-icon" viewBox="0 0 32 32" aria-hidden="true">
          <circle cx="16" cy="16" r="16" fill="var(--ink-light)"/>
          <path d="M11.2 8.6c.5-.4 1.2-.3 1.5.2l1.7 2.6c.3.5.2 1.1-.2 1.5l-1.1.9c.8 1.9 2.4 3.6 4.4 4.6l.9-1.1c.4-.4 1-.5 1.5-.2l2.6 1.6c.5.3.7 1 .3 1.5l-1.2 1.7c-.6.8-1.6 1.1-2.5.8-4.3-1.5-7.6-4.9-9-9.2-.3-.9 0-1.9.8-2.5z" fill="var(--icon-glyph)"/>
        </svg>
        <span>323-481-5206</span>
      </li>
      <li class="contact-item">
        <svg class="contact-icon" viewBox="0 0 32 32" aria-hidden="true">
          <circle cx="16" cy="16" r="16" fill="var(--ink-light)"/>
          <rect x="8.5" y="10.5" width="15" height="11" rx="1" fill="none" stroke="var(--icon-glyph)" stroke-width="1.8"/>
          <path d="M9 11.5l7 5.5 7-5.5" fill="none" stroke="var(--icon-glyph)" stroke-width="1.8"/>
        </svg>
        <span>owentaskerlens@mailbox-example.net</span>
      </li>
      <li class="contact-item">
        <svg class="contact-icon" viewBox="0 0 32 32" aria-hidden="true">
          <circle cx="16" cy="16" r="16" fill="var(--ink-light)"/>
          <circle cx="16" cy="16" r="7.5" fill="var(--icon-glyph)"/>
          <path d="M12.5 12.5c1.5-.5 2.5.3 2.2 1.6-.3 1.1.9 1.5 1.6 2.3.6.8-.3 2-1.2 2.4M18.5 10.5c.3 1.2 1.4 1.5 2.2 1.2" fill="none" stroke="var(--ink-light)" stroke-width="1.1"/>
        </svg>
        <span>taskerlens.examplefolio.net</span>
      </li>
    </ul>
  </section>

  <section class="card card--back" aria-label="Business card back">
    <p class="logo-name">Owen Tasker Studios</p>
  </section>
</main>
</body>
</html>
```